recreate a simple image with minor flat

I really like the image on this book cover (Tidemark) and would like to make it into a poster. Please recreate a black on white version of this with a similar arrow and emphasis. You may detail the archer differently. I view this image as aspirational, with an Copper-fallen like character pushing himself to "Aim Higher." Thank you!

```html
<!DOCTYPE html>
<html lang="en">
<head>
<meta charset="utf-8">
<title>Aim Higher Poster</title>
<link rel="stylesheet" href="https://fonts.googleapis.com/css2?family=Rubik+Dirt&family=Bebas+Neue&family=Cormorant+Garamond:wght@500&display=swap">
<style>
  :root {
    --ink: #0a0a0a;
    --paper: #ffffff;
    --ray: #f0f0f0;
    --ray-soft: #f6f6f6;
    --arrow-dark: #231f20;
    --arrow-light: #e6e6e6;
    --figure: #d9d9d9;
  }
  html, body {
    margin: 0;
    padding: 0;
    width: 926px;
    height: 1200px;
    overflow: hidden;
    background: var(--paper);
  }
  .poster {
    position: relative;
    width: 926px;
    height: 1200px;
    background: var(--paper);
    overflow: hidden;
  }
  .poster__art {
    position: absolute;
    inset: 0;
  }
  .headline {
    position: absolute;
    left: 72px;
    top: 52px;
    margin: 0;
    font-family: "Rubik Dirt", "Impact", sans-serif;
    font-weight: 400;
    color: var(--ink);
    line-height: 1;
    transform-origin: left top;
    transform: scaleX(0.78);
  }
  .headline__top {
    display: block;
    font-size: 88px;
    letter-spacing: 2px;
  }
  .headline__bottom {
    display: block;
    font-size: 184px;
    margin-top: -10px;
    letter-spacing: 2px;
  }
  .intro {
    position: absolute;
    left: 83px;
    top: 296px;
    width: 340px;
    margin: 0;
    font-family: "Cormorant Garamond", "Georgia", serif;
    font-weight: 500;
    font-size: 19.5px;
    line-height: 23px;
    color: var(--ink);
  }
  .aside {
    position: absolute;
    left: 560px;
    top: 1016px;
    width: 290px;
  }
  .aside__title {
    margin: 0;
    font-family: "Bebas Neue", "Arial Narrow", sans-serif;
    font-weight: 400;
    font-size: 52px;
    line-height: 1;
    color: var(--ink);
    letter-spacing: 0.5px;
  }
  .aside__body {
    margin: 8px 0 0;
    font-family: "Cormorant Garamond", "Georgia", serif;
    font-weight: 500;
    font-size: 19.5px;
    line-height: 23px;
    color: var(--ink);
  }
</style>
</head>
<body>
<main class="poster">
  <svg class="poster__art" width="926" height="1200" viewBox="0 0 926 1200" xmlns="http://www.w3.org/2000/svg">
    <defs>
      <linearGradient id="arrow-fade" x1="193" y1="869" x2="860" y2="62" gradientUnits="userSpaceOnUse">
        <stop offset="0" stop-color="var(--arrow-light)" stop-color-fallback="#e6e6e6"/>
        <stop offset="0.45" stop-color="#9e9e9e"/>
        <stop offset="1" stop-color="#231f20"/>
      </linearGradient>
    </defs>

    <g class="rays">
      <polygon points="870,40 27,70 27,110 " fill="var(--ray-soft)"/>
      <polygon points="870,40 27,230 27,370" fill="var(--ray)"/>
      <polygon points="870,40 27,540 27,720" fill="var(--ray-soft)"/>
      <polygon points="870,40 27,950 100,1165 180,1165" fill="var(--ray)"/>
      <polygon points="870,40 320,1165 510,1165" fill="var(--ray-soft)"/>
      <polygon points="870,40 700,1165 886,1165 886,250" fill="var(--ray)"/>
    </g>

    <polygon class="aim-arrow"
      points="193,869 748,145 713,120 860,62 841,209 808,187"
      fill="url(#arrow-fade)"/>

    <rect class="archer-figure" role="img" aria-label="Silhouette of a muscular archer drawing a bow, aiming upward"
      x="82" y="866" width="136" height="238" rx="4" fill="var(--figure)"/>

    <rect class="frame" x="24.5" y="27.5" width="864" height="1140" fill="none" stroke="var(--ink)" stroke-width="5"/>
  </svg>

  <h1 class="headline">
    <span class="headline__top">YOUR TEXT</span>
    <span class="headline__bottom">HERE</span>
  </h1>

  <p class="intro">Lorem ipsum dolor sit amet, consectetuer adipiscing elit, sed diam nonummy nibh euismod tincidunt ut laoreet dolore</p>

  <section class="aside">
    <h2 class="aside__title">YOUR TEXT HERE</h2>
    <p class="aside__body">Lorem ipsum dolor sit amet, consectetuer adipiscing elit, sed diam nonummy nibh euismod tincidunt ut laoreet dolore magna aliquam</p>
  </section>
</main>
</body>
</html>
```